MMA fitness boot camp

We need a flyer that feels friendly and inviting to people who have never done fitness or training before. It also needs to look serious so it has the look of being a serious workout program.

We dont mind how it is set out as long as it conveys the message.

We do not want images of professional MMA fighters fighting. We like fitness training images that are relatable. eg- fit women punching or kicking a punching bag . If possible add men as well. We are aiming for men and women to do the boot camp.

The information for flyer is as below-

‘MMA Fitness Bootcamp’

Join us at Ironleaf Combat Studio for our new Mixed Martial Arts Bootcamp. You will train for 4 weeks with the same fitness methods a professional fighter would use before a fight! You will get an intense and challenging workout whilst having fun. This isn’t your common boot camp held at the local park, this is unique and enjoyable!

During this 4 week period, you will be training twice a week early mornings in our Training facility.

Enjoy training in a supportive environment with an MMA fighter and qualified Master trainer pushing you every session so that you get the best out of yourself.

For more information email us at marcus@ironleafcombatstudio.com.au or to book your spot with us.

or visit us at-
www.ironleafcombatstudio.com

ALL FITNESS LEVELS WELCOME!

Level 1, 274 Penrow Rd. Smithfield.'

```html
<!DOCTYPE html>
<html lang="en">
<head>
<meta charset="utf-8">
<title>MMA Fitness Bootcamp Flyer Options</title>
<link href="https://fonts.googleapis.com/css2?family=Oswald:wght@500;600&family=Archivo+Black&display=swap" rel="stylesheet">
<style>
  :root {
    --orange: #f29422;
    --black: #1c1a1a;
    --white: #ffffff;
    --ink: #2b2b2b;
    --stage: #e9e6e1;
  }
  * { margin: 0; padding: 0; box-sizing: border-box; }
  html, body { width: 1200px; height: 900px; overflow: hidden; }
  body { background: var(--stage); font-family: Arial, Helvetica, sans-serif; position: relative; }

  .option-label {
    position: absolute; top: 30px; width: 376px; text-align: center;
    font-family: "Archivo Black", Arial, sans-serif; font-size: 38px; color: var(--ink); letter-spacing: 0.5px;
  }
  .option-label--one { left: 201px; }
  .option-label--two { left: 670px; }

  .flyer { position: absolute; top: 80px; width: 376px; height: 788px; background: var(--white); overflow: hidden; }
  .flyer--one { left: 201px; }
  .flyer--two { left: 670px; }
  .flyer__frame { position: absolute; inset: 0; }

  .studio-name {
    position: absolute; top: 48px; left: 0; width: 376px; text-align: center;
    font-family: "Oswald", Arial, sans-serif; font-weight: 600; font-size: 25px; color: var(--orange); text-transform: uppercase;
  }
  .photo { position: absolute; z-index: 1; }
  .flyer--one .photo { left: 27px; top: 154px; width: 324px; height: 261px;
    background: linear-gradient(160deg, #c9c3bd 0%, #8f8a86 45%, #5a5552 100%); }
  .flyer--two .photo { left: 25px; top: 174px; width: 326px; height: 203px;
    background: radial-gradient(ellipse at 30% 50%, #7a5a44 0%, #2a2220 55%, #141212 100%); }

  .flyer__title {
    position: absolute; left: 0; width: 376px; text-align: center; z-index: 2;
    font-family: "Oswald", Arial, sans-serif; font-weight: 500; font-size: 30px; line-height: 32px;
    color: var(--orange); letter-spacing: 0.3px; transform: scaleX(0.9);
  }
  .flyer--one .flyer__title { top: 120px; }
  .flyer--two .flyer__title { top: 118px; }

  .join-banner { position: absolute; background: var(--orange); text-align: center; z-index: 2; }
  .flyer--one .join-banner { left: 15px; top: 415px; width: 347px; height: 80px; padding-top: 8px; }
  .flyer--two .join-banner { left: 15px; top: 376px; width: 345px; height: 74px; padding-top: 7px; }
  .join-banner__lead {
    font-family: "Oswald", Arial, sans-serif; font-weight: 500; font-size: 22px; line-height: 24px;
    text-transform: uppercase; transform: scaleX(0.88);
  }
  .join-banner__lead strong { font-size: 26px; font-weight: 600; }
  .join-banner__sub { font-weight: 700; font-size: 15px; line-height: 17px; text-transform: uppercase; }
  .flyer--one .join-banner__lead, .flyer--one .join-banner__sub { color: var(--black); }
  .flyer--two .join-banner__lead, .flyer--two .join-banner__sub { color: var(--white); }

  .details { position: absolute; color: var(--white); font-size: 13.4px; line-height: 15.6px; z-index: 2; }
  .flyer--one .details { left: 34px; top: 498px; width: 302px; }
  .flyer--two .details { left: 33px; top: 466px; width: 304px; }
  .details p { margin-bottom: 6px; }

  .contact { position: absolute; left: 0; width: 376px; text-align: center; z-index: 2; }
  .flyer--one .contact { top: 718px; }
  .flyer--two .contact { top: 716px; }
  .contact__heading {
    font-family: "Oswald", Arial, sans-serif; font-weight: 500; font-size: 20px; line-height: 22px;
    color: var(--orange); text-transform: uppercase; transform: scaleX(0.88);
  }
  .contact__line { font-size: 11px; line-height: 12px; color: var(--black); }
</style>
</head>
<body>

<div class="option-label option-label--one">OPTION-1</div>
<div class="option-label option-label--two">OPTION-2</div>

<article class="flyer flyer--one">
  <svg class="flyer__frame" width="376" height="788" viewBox="0 0 376 788" aria-hidden="true">
    <rect x="0" y="198" width="376" height="50" fill="var(--orange)"/>
    <rect x="0" y="320" width="376" height="95" fill="var(--orange)"/>
    <rect x="0" y="500" width="376" height="92" fill="var(--orange)"/>
    <path d="M27 75 Q27 40 45 35 L331 35 Q351 40 351 75 L351 760 L27 760 Z" fill="var(--black)"/>
    <path d="M45 0 L331 0 L331 85 Q331 112 304 112 L72 112 Q45 112 45 85 Z" fill="var(--white)"/>
    <path d="M50 760 L50 735 Q50 712 78 712 L298 712 Q326 712 326 735 L326 760 Z" fill="var(--white)"/>
    <rect x="0" y="740" width="376" height="48" fill="var(--white)"/>
  </svg>
  <div class="studio-name">Ironleaf Combat Studio</div>
  <div class="photo" role="img" aria-label="Photo of a fit woman lifting a barbell overhead in a gym"></div>
  <h1 class="flyer__title">MMA FITNESS BOOTCAMP</h1>
  <div class="join-banner">
    <div class="join-banner__lead"><strong>Join Us</strong> at Ironleaf Combat Studio</div>
    <div class="join-banner__sub">For our new Mixed Martial Arts<br>Bootcamp</div>
  </div>
  <div class="details">
    <p>You will train for <b>4 weeks</b> with the same fitness methods a professional fighter would use before a fight! You will get an intense and challenging workout whilst having fun. <b>This isn’t your common boot camp held at the local park, this is unique and enjoyable!</b></p>
    <p>During this 4 week period, you will be training twice a week early mornings in our Training facility.</p>
    <p>Enjoy training in a supportive environment with an MMA fighter and qualified Master trainer pushing you every session so that you get the best out of yourself.</p>
  </div>
  <div class="contact">
    <div class="contact__heading">For more information email us at</div>
    <div class="contact__line">marcus@ironleafcombatstudio.com.au</div>
    <div class="contact__heading">Visit our website</div>
    <div class="contact__line">www.ironleafcombatstudio.com</div>
  </div>
</article>

<article class="flyer flyer--two">
  <svg class="flyer__frame" width="376" height="788" viewBox="0 0 376 788" aria-hidden="true">
    <rect x="0" y="195" width="376" height="105" fill="var(--orange)"/>
    <path d="M25 75 Q25 40 43 35 L333 35 Q351 40 351 75 L351 760 L25 760 Z" fill="var(--black)"/>
    <path d="M45 0 L331 0 L331 85 Q331 112 304 112 L72 112 Q45 112 45 85 Z" fill="var(--white)"/>
    <path d="M48 760 L48 732 Q48 708 76 708 L300 708 Q328 708 328 732 L328 760 Z" fill="var(--white)"/>
    <rect x="0" y="740" width="376" height="48" fill="var(--white)"/>
  </svg>
  <div class="studio-name">Ironleaf Combat Studio</div>
  <div class="photo" role="img" aria-label="Photo of a muscular man with a dumbbell and a fit woman with wrapped hands"></div>
  <h1 class="flyer__title">MMA FITNESS BOOTCAMP</h1>
  <div class="join-banner">
    <div class="join-banner__lead"><strong>Join Us</strong> at Ironleaf Combat Studio</div>
    <div class="join-banner__sub">For our new Mixed Martial Arts<br>Bootcamp</div>
  </div>
  <div class="details">
    <p>You will train for <b>4 weeks</b> with the same fitness methods a professional fighter would use before a fight! You will get an intense and challenging workout whilst having fun. <b>This isn’t your common boot camp held at the local park, this is unique and enjoyable!</b></p>
    <p>During this 4 week period, you will be training twice a week early mornings in our Training facility.</p>
    <p>Enjoy training in a supportive environment with an MMA fighter and qualified Master trainer pushing you every session so that you get the best out of yourself.</p>
  </div>
  <div class="contact">
    <div class="contact__heading">For more information email us at</div>
    <div class="contact__line">marcus@ironleafcombatstudio.com.au</div>
    <div class="contact__heading">Visit our website</div>
    <div class="contact__line">www.ironleafcombatstudio.com</div>
  </div>
</article>

</body>
</html>
```